Online Psychology Practice needs business cards.

Online Psychology service needs business cards. Have own logo- please see uploaded. I have other file formats if you need (not sure one needed?)

Details for Business Card:
Fiona Kettlewood
Clinical Psychologist BPsych, BPsych (Hons), MPsych (Clin), MAPS
T: 0457260714 | F: 08 71526804
E: hello@harbourlightmindcarestudio.com.au
W: harbourlightmindcarestudio.com.au

Industry/Entity Type

Health

Contact Information for Business Card

Logo plus details above (couldn't write in this section)

```html
<!DOCTYPE html>
<html lang="en">
<head>
<meta charset="utf-8">
<title>Harbourlight Mindcare Studio – Business Cards</title>
<link href="https://fonts.googleapis.com/css2?family=Roboto:wght@400;500;700&family=Roboto+Condensed:wght@700&display=swap" rel="stylesheet">
<style>
  :root {
    --backdrop: #3b3b3b;
    --card: #141414;
    --edge: #1597c4;
    --brand-blue: #1a8fc0;
    --brand-deep: #1c5f92;
    --text-light: #e9e9e9;
    --emboss: #2b2b2b;
  }
  * { margin: 0; padding: 0; box-sizing: border-box; }
  html, body {
    width: 1200px; height: 801px; overflow: hidden;
    background: var(--backdrop);
    font-family: "Roboto", Arial, sans-serif;
  }
  .stage {
    position: relative; width: 1200px; height: 801px;
    display: flex; align-items: center; justify-content: center; gap: 44px;
  }
  .card {
    position: relative; width: 540px; height: 310px;
    background: var(--card);
    border-bottom: 3px solid var(--edge);
    border-left: 2px solid var(--edge);
    overflow: hidden;
  }

  /* Front */
  .brand-mark {
    position: absolute; right: 46px; top: 34px;
    width: 150px; height: 150px; border-radius: 50%;
    background: var(--brand-deep);
  }
  .brand-name {
    position: absolute; left: 34px; top: 40px;
    font-family: "Roboto", Arial, sans-serif;
    font-weight: 500; font-size: 21px; line-height: 1.2;
    letter-spacing: 2px; text-transform: uppercase;
    color: var(--brand-blue);
  }
  .person { position: absolute; left: 34px; top: 124px; }
  .person-name {
    font-family: "Roboto Condensed", "Arial Narrow", sans-serif;
    font-weight: 700; font-size: 20px; text-transform: uppercase;
    color: var(--brand-blue); letter-spacing: 0.3px;
  }
  .person-role {
    font-size: 12.5px; line-height: 1.45; color: var(--text-light); margin-top: 4px;
  }
  .contacts {
    position: absolute; left: 34px; top: 206px; list-style: none;
    font-size: 12.5px; color: var(--text-light);
  }
  .contacts li { display: flex; align-items: center; gap: 8px; line-height: 1.55; }
  .contacts svg { width: 11px; height: 11px; fill: var(--brand-blue); flex: none; }

  /* Back */
  .card-back { display: flex; flex-direction: column; align-items: center; justify-content: center; gap: 18px; }
  .back-mark { width: 74px; height: 74px; border-radius: 50%; background: var(--emboss); }
  .back-name {
    font-family: "Roboto", Arial, sans-serif; font-weight: 500;
    font-size: 24px; letter-spacing: 2.5px; text-transform: uppercase;
    color: var(--emboss); text-align: center; line-height: 1.2;
  }
</style>
</head>
<body>
<main class="stage">

  <section class="card card-front" aria-label="Business card front">
    <div class="brand-mark"></div>
    <div class="brand-name">Harbourlight<br>Mindcare Studio</div>

    <div class="person">
      <div class="person-name">Fiona Kettlewood</div>
      <div class="person-role">Clinical Psychologist BPsych<br>BPsych (Hons), MPsych (Clin), MAPS</div>
    </div>

    <ul class="contacts">
      <li>
        <svg viewBox="0 0 24 24" aria-hidden="true"><path d="M6.6 10.8a15.1 15.1 0 0 0 6.6 6.6l2.2-2.2a1 1 0 0 1 1-.25 11.4 11.4 0 0 0 3.6.57 1 1 0 0 1 1 1V20a1 1 0 0 1-1 1A17 17 0 0 1 3 4a1 1 0 0 1 1-1h3.5a1 1 0 0 1 1 1c0 1.25.2 2.45.57 3.6a1 1 0 0 1-.25 1z"/></svg>
        0457260714
      </li>
      <li>
        <svg viewBox="0 0 24 24" aria-hidden="true"><path d="M6 2h10l2 2v5H6zM3 10h18a1 1 0 0 1 1 1v7h-4v4H6v-4H2v-7a1 1 0 0 1 1-1zm5 7v3h8v-3z"/></svg>
        08 71526804
      </li>
      <li>
        <svg viewBox="0 0 24 24" aria-hidden="true"><path d="M2 5h20v14H2zm2 2v.5l8 5 8-5V7l-8 5z"/></svg>
        hello@harbourlightmindcarestudio.com.au
      </li>
      <li>
        <svg viewBox="0 0 24 24" aria-hidden="true"><path d="M12 2a10 10 0 1 0 0 20 10 10 0 0 0 0-20zm6.9 6h-3a15 15 0 0 0-1.3-4A8 8 0 0 1 18.9 8zM12 4c.8 1.1 1.5 2.5 1.9 4h-3.8c.4-1.5 1.1-2.9 1.9-4zM4.3 14a8 8 0 0 1 0-4h3.4a16 16 0 0 0 0 4zm.8 2h3a15 15 0 0 0 1.3 4A8 8 0 0 1 5.1 16zm3-8h-3a8 8 0 0 1 4.3-4 15 15 0 0 0-1.3 4zM12 20c-.8-1.1-1.5-2.5-1.9-4h3.8c-.4 1.5-1.1 2.9-1.9 4zm2.3-6H9.7a14 14 0 0 1 0-4h4.6a14 14 0 0 1 0 4zm.3 6a15 15 0 0 0 1.3-4h3a8 8 0 0 1-4.3 4zm1.7-6a16 16 0 0 0 0-4h3.4a8 8 0 0 1 0 4z"/></svg>
        harbourlightmindcarestudio.com.au
      </li>
    </ul>
  </section>

  <section class="card card-back" aria-label="Business card back">
    <div class="back-mark"></div>
    <div class="back-name">Harbourlight<br>Mindcare Studio</div>
  </section>

</main>
</body>
</html>
```